Criação de Papelaria Profissional para Consultoria de Negócios
A empresa queria:
" Serviços de Consultoria de Carreira (transição, desenvolvimento de liderança), Assessment, Coaching, Outplacement, Headhunting "

```html
<!DOCTYPE html>
<html lang="pt-BR">
<head>
<meta charset="UTF-8">
<title>Papel Timbrado – Lívia Marchetti Consultores de Carreira</title>
<link href="https://fonts.googleapis.com/css2?family=Montserrat:wght@300;400;500;600&display=swap" rel="stylesheet">
<style>
  :root {
    --backdrop: #e9e6e2;
    --paper: #ffffff;
    --ink: #2b2b2b;
    --brand: #5a2a2e;
    --accent: #b3303c;
    --muted: #6f6f6f;
    --band: #bdbdbd;
    --rule: #dddddd;
  }
  * { margin: 0; padding: 0; box-sizing: border-box; }
  html, body {
    width: 1200px; height: 1200px; overflow: hidden;
    background: var(--backdrop);
    font-family: "Montserrat", sans-serif;
    color: var(--ink);
  }
  .letterhead {
    position: absolute; left: 204px; top: 40px;
    width: 792px; height: 1120px;
    background: var(--paper);
    box-shadow: 0 6px 24px rgba(0,0,0,.18);
  }
  .brand {
    position: absolute; top: 78px; left: 0; width: 100%;
    text-align: center; color: var(--brand);
  }
  .brand-name {
    display: inline-flex; align-items: center; gap: 10px;
    font-size: 27px; font-weight: 400; letter-spacing: 1px;
    text-transform: uppercase;
  }
  .brand-dot { width: 12px; height: 12px; border-radius: 50%; background: var(--brand); }
  .brand-tagline {
    margin-top: 4px; font-size: 9px; letter-spacing: 3px;
    text-transform: uppercase; font-weight: 500;
  }
  .title {
    position: absolute; left: 60px; top: 212px;
    font-size: 40px; font-weight: 400; letter-spacing: 1px;
  }
  .body {
    position: absolute; left: 60px; top: 300px; width: 672px;
    font-size: 12.6px; line-height: 19px; text-align: justify;
  }
  .body p { margin-bottom: 19px; }
  .signature {
    position: absolute; left: 330px; top: 912px;
    width: 150px; height: 76px;
    background: linear-gradient(135deg, #e6e6e6, #cfcfcf);
    border-radius: 6px;
  }
  .signer {
    position: absolute; left: 0; top: 996px; width: 100%;
    text-align: center; font-size: 12px; font-weight: 600; line-height: 15px;
  }
  .signer .role { display: block; color: var(--accent); font-weight: 400; font-size: 11px; }
  .footer {
    position: absolute; left: 40px; right: 40px; top: 1044px;
    display: flex; justify-content: space-between; align-items: center;
    font-size: 10px; font-weight: 500; text-transform: uppercase;
    border-top: 1px solid var(--rule); padding-top: 10px;
  }
  .contact { display: flex; align-items: center; gap: 7px; }
  .contact svg { width: 16px; height: 16px; fill: var(--accent); flex: none; }
  .contact-stack { line-height: 14px; }
  .address { line-height: 13px; font-size: 9.5px; }
  .address b { font-weight: 600; }
  .base-band {
    position: absolute; left: 230px; right: 230px; bottom: 0; height: 22px;
    background: var(--band); border-radius: 10px 10px 0 0;
  }
</style>
</head>
<body>
<main class="letterhead">
  <header class="brand">
    <div class="brand-name"><span class="brand-dot"></span>Lívia Marchetti</div>
    <div class="brand-tagline">Consultores de Carreira</div>
  </header>

  <h1 class="title">TÍTULO</h1>

  <section class="body">
    <p>Lorem Ipsum é simplesmente uma simulação de texto da indústria tipográfica e de impressos, e vem sendo utilizado desde o século XVI, quando um impressor desconhecido pegou uma bandeja de tipos e os embaralhou para fazer um livro de modelos de tipos. Lorem Ipsum sobreviveu não só a cinco séculos, como também ao salto para a editoração eletrônica, permanecendo essencialmente inalterado. Se popularizou na década de 60, quando a Tipografix lançou decalques contendo passagens de Lorem Ipsum, e mais recentemente quando passou a ser integrado a softwares de editoração eletrônica como Compositor Pro.</p>
    <p>Lorem Ipsum é simplesmente uma simulação de texto da indústria tipográfica e de impressos, e vem sendo utilizado desde o século XVI, quando um impressor desconhecido pegou uma bandeja de tipos e os embaralhou para fazer um livro de modelos de tipos. Lorem Ipsum sobreviveu não só a cinco séculos, como também ao salto para a editoração eletrônica, permanecendo essencialmente inalterado. Se popularizou na década de 60, quando</p>
    <p>Lorem Ipsum é simplesmente uma simulação de texto da indústria tipográfica e de impressos, e vem sendo utilizado desde o século XVI, quando um impressor desconhecido pegou uma bandeja de tipos e os embaralhou para fazer</p>
    <p>Lorem Ipsum é simplesmente uma simulação de texto da indústria tipográfica e de impressos, e vem sendo utilizado desde o século XVI, quando um impressor desconhecido pegou uma bandeja de tipos e os embaralhou para fazer</p>
    <p>Lorem Ipsum é simplesmente uma simulação de texto da indústria tipográfica e de impressos, e vem sendo utilizado desde o século XVI, quando um impressor desconhecido pegou uma bandeja de tipos e os embaralhou para fazer</p>
    <p>Lorem Ipsum é simplesmente uma simulação de texto da indústria tipográfica e de impressos, e vem sendo utilizado desde o século XVI, quando um impressor desconhecido pegou uma bandeja de tipos e os embaralhou para fazer</p>
  </section>

  <div class="signature" role="img" aria-label="Assinatura manuscrita do responsável"></div>
  <div class="signer">Nome do Responsável<span class="role">Cargo</span></div>

  <footer class="footer">
    <div class="contact">
      <svg viewBox="0 0 24 24" aria-hidden="true"><path d="M6.6 10.8a15.1 15.1 0 0 0 6.6 6.6l2.2-2.2c.3-.3.7-.4 1-.2 1.1.4 2.3.6 3.6.6.6 0 1 .4 1 1V20c0 .6-.4 1-1 1C10.6 21 3 13.4 3 4c0-.6.4-1 1-1h3.5c.6 0 1 .4 1 1 0 1.3.2 2.5.6 3.6.1.3 0 .7-.2 1z"/></svg>
      <span>marchetticarreira.com.br</span>
    </div>
    <div class="contact">
      <svg viewBox="0 0 24 24" aria-hidden="true"><path d="M3 5h18v14H3z M3 5l9 7 9-7" fill="none" stroke="#b3303c" stroke-width="2"/></svg>
      <span class="contact-stack">marchetticarreira.com.br<br>contato@marchetticarreira.com.br</span>
    </div>
    <div class="contact">
      <svg viewBox="0 0 24 24" aria-hidden="true"><path d="M12 2a7 7 0 0 0-7 7c0 5.3 7 13 7 13s7-7.7 7-13a7 7 0 0 0-7-7zm0 9.5A2.5 2.5 0 1 1 12 6.5a2.5 2.5 0 0 1 0 5z"/></svg>
      <span class="address"><b>Nome da Rua, 000</b> - Bairro<br><b>Cidade</b> - Estado - CEP e País</span>
    </div>
  </footer>

  <div class="base-band"></div>
</main>
</body>
</html>
```